Refresh Home Page for Photography Training Site

http://brannockcourses.example/

My site is looking kind of out-of-date, so it's time for a face lift. I want to bring it up to date with a more modern web look.

What I need from you is a home page design concept. No coding, just a PSD design, but it MUST be something that a coder could build into an efficient, fast-loading page. After the home page design contest is finished, we can work together privately, if you want to continue, to design the rest of the pages in the site for additional fees.

Functionally, the new page needs to do the same job as the current home page, just do it more efficiently (if possible) while looking fresh and modern.

Sites I like
http://vantri.example/ (clean, modern)

Competitor sites:
http://dorwinlessons.example/
http://www.glenmarshallphotography.example/

Target Market(s)

Amateur and semi-professional photographers

Industry/Entity Type

Training

Requirements
Must have
• MUST HAVE
1. A prominent space where testimonials appear in rotation, one after another (instead of the one large testimonial on the current site).

2. My photo in the header. It can be smaller than at present. If you prefer you can use the black and white photo from the about page. Put a signature saying Ron Brannock near the photo, in a better handwritten style than the current signature, which is a lame font.

3. Tagline "Learn Photography and Image Editing the Easy Way"
Should not have
• No flash or other fancy technology. (However it is acceptable to design an area that would be an image carousel, where one image changes to another, then another, etc. Like the Glen Marshall or Vantri site. That is not too fancy, but it's optional).

```html
<!DOCTYPE html>
<html lang="en">
<head>
<meta charset="utf-8">
<title>Ron Brannock — Learn Photography and Image Editing the Easy Way</title>
<link href="https://fonts.googleapis.com/css2?family=Arimo:wght@400;700&display=swap" rel="stylesheet">
<style>
  :root {
    --page-bg: #121212;
    --panel-bg: #0d0d0d;
    --panel-border: #262626;
    --topbar-top: #2a2a2a;
    --topbar-bottom: #101010;
    --nav-top: #2e2e2e;
    --nav-bottom: #161616;
    --nav-divider: #3a3a3a;
    --brand-blue: #0b44b0;
    --brand-blue-dark: #07307e;
    --text-light: #ffffff;
    --text-muted: #9a9a9a;
    --text-dim: #6f6f6f;
    --card-bg: #262626;
    --card-border: #363636;
    --social-blue: #3b5ba0;
    --social-sky: #3aa0d8;
    --social-orange: #e8761c;
  }
  * { box-sizing: border-box; margin: 0; padding: 0; }
  html, body { width: 1024px; height: 1200px; overflow: hidden; }
  body {
    background: var(--page-bg);
    font-family: "Arimo", Arial, sans-serif;
    color: var(--text-muted);
    position: relative;
  }
  .topbar {
    position: absolute; left: 0; top: 0; width: 1024px; height: 34px;
    background: linear-gradient(var(--topbar-top), var(--topbar-bottom));
    font-size: 12px; color: var(--text-muted);
  }
  .topbar .date { position: absolute; left: 50px; top: 11px; }
  .topbar .social { position: absolute; left: 244px; top: 10px; display: flex; gap: 14px; }
  .topbar .account { position: absolute; right: 50px; top: 11px; }
  .topbar .account span { margin: 0 6px; color: var(--text-dim); }
  .dot { width: 13px; height: 13px; border-radius: 2px; display: block; }
  .dot.blue { background: var(--social-blue); }
  .dot.sky { background: var(--social-sky); }
  .dot.orange { background: var(--social-orange); }

  .header-portrait {
    position: absolute; left: 46px; top: 61px; width: 80px; height: 89px;
    background: radial-gradient(circle at 50% 40%, #9a9a9a, #3a3a3a 70%, #161616);
  }
  .signature {
    position: absolute; left: 130px; top: 124px; font-size: 14px; color: #cfcfcf;
  }
  .tagline {
    position: absolute; left: 206px; top: 76px; font-size: 24px; font-weight: 700;
    color: var(--text-light); letter-spacing: 0.2px;
  }

  .main {
    position: absolute; left: 34px; top: 153px; width: 958px; height: 969px;
    background: var(--panel-bg); border: 1px solid var(--panel-border);
  }
  .nav {
    position: absolute; left: 13px; top: 13px; width: 931px; height: 45px;
    background: linear-gradient(var(--nav-top), var(--nav-bottom));
    border-bottom: 5px solid var(--brand-blue);
    display: flex;
  }
  .nav a {
    color: var(--text-light); text-decoration: none; font-size: 14px;
    padding: 0 23px; line-height: 40px; border-right: 1px solid var(--nav-divider);
  }
  .nav a.active { background: var(--brand-blue); border-right: none; }
  .search {
    position: absolute; right: 9px; top: 6px; width: 188px; height: 26px;
    background: #4a4a4a; border: 1px solid #5a5a5a; color: #bbb; font-size: 12px;
    padding: 6px 10px;
  }
  .search svg { position: absolute; right: 0; top: 0; width: 26px; height: 24px; background: #5d5d5d; }

  .hero {
    position: absolute; left: 13px; top: 58px; width: 931px; height: 326px;
    background: linear-gradient(90deg, #5f7b36 0%, #8c7a5a 35%, #c7a383 65%, #6e8d6a 100%);
  }
  .hero .dots { position: absolute; right: 82px; bottom: 54px; display: flex; gap: 8px; }
  .hero .dots i { width: 10px; height: 10px; border-radius: 50%; background: rgba(255,255,255,.5); display: block; }
  .hero .dots i:first-child { background: #fff; }

  .newsletter {
    position: absolute; left: 13px; top: 384px; width: 931px; height: 57px;
    background: linear-gradient(var(--brand-blue), var(--brand-blue-dark));
  }
  .newsletter p { position: absolute; left: 19px; top: 20px; font-size: 16px; font-weight: 700; color: var(--text-light); }
  .newsletter .email {
    position: absolute; left: 574px; top: 15px; width: 189px; height: 28px;
    background: #fff; border-radius: 3px; font-size: 12px; color: #aaa; padding: 8px 14px;
  }
  .newsletter .subscribe {
    position: absolute; left: 774px; top: 9px; width: 131px; height: 38px;
    background: linear-gradient(#2b2b2b, #050505); border-radius: 4px; border: 1px solid #000;
    color: #fff; font-size: 17px; font-weight: 700; text-align: center; line-height: 36px;
  }

  .feature {
    position: absolute; top: 468px; height: 133px; background: var(--card-bg);
    border: 1px solid var(--card-border);
  }
  .feature .thumb { position: absolute; left: 0; top: 0; width: 133px; height: 131px; }
  .feature h3 {
    position: absolute; left: 146px; top: 14px; font-size: 18px; font-weight: 400;
    color: #d8d8d8; line-height: 23px; text-transform: uppercase;
  }
  .feature .more { position: absolute; right: 16px; bottom: 12px; font-size: 9px; font-weight: 700; letter-spacing: 1.5px; color: #aaa; }
  .f1 { left: 13px; width: 278px; }
  .f2 { left: 337px; width: 282px; }
  .f3 { left: 663px; width: 281px; }
  .f1 .thumb { background: linear-gradient(#3d86c8, #1c5f9e); }
  .f2 .thumb { background: linear-gradient(135deg, #f2f2f2, #5a4436 60%, #1a1a1a); }
  .f3 .thumb { background: linear-gradient(#f0f0f0, #c2b8a8); }

  .body-copy {
    position: absolute; left: 16px; top: 644px; width: 620px; font-size: 12px;
    line-height: 20.5px; color: #aaaaaa;
  }
  .body-copy p + p { margin-top: 20px; }

  .video {
    position: absolute; left: 656px; top: 644px; width: 288px; height: 143px;
    background: linear-gradient(90deg, #e6e2ea, #6b7fb0 40%, #3b76c4 70%, #c083c4);
    border: 3px solid #262626;
  }
  .video svg { position: absolute; left: 117px; top: 44px; }

  .quote {
    position: absolute; left: 656px; top: 824px; width: 284px; height: 76px;
    background: #1e1e1e; border: 2px solid #444; border-radius: 6px;
    font-size: 12px; line-height: 20px; color: #9a9a9a; padding: 12px 14px 0 32px;
  }
  .quote .mark { position: absolute; left: 9px; top: 4px; font-size: 32px; font-weight: 700; color: #666; }
  .quote svg { position: absolute; right: 18px; bottom: -16px; }
  .author { position: absolute; left: 656px; top: 922px; width: 284px; text-align: right; padding-right: 18px; font-size: 12px; }
  .author strong { display: block; color: #cfcfcf; }
  .author span { display: block; margin-top: 6px; margin-right: 24px; color: #8a8a8a; }

  .footer { position: absolute; left: 0; top: 1122px; width: 1024px; height: 78px; background: #0e0e0e; border-top: 2px solid #2a2a2a; }
  .footer .links { position: absolute; left: 41px; top: 17px; font-size: 11px; color: #9a9a9a; }
  .footer .links span { margin: 0 10px; color: #666; }
  .footer .copy { position: absolute; left: 41px; top: 42px; font-size: 11px; color: #666; }
  .footer .social { position: absolute; left: 876px; top: 17px; display: flex; gap: 20px; }
  .footer .social .dot { width: 20px; height: 20px; border-radius: 3px; }
</style>
</head>
<body>
  <div class="topbar">
    <span class="date">Wednesday, September 21, 2011</span>
    <div class="social" aria-hidden="true"><i class="dot blue"></i><i class="dot sky"></i><i class="dot orange"></i></div>
    <div class="account">Log in<span>|</span>Register</div>
  </div>

  <div class="header-portrait" role="img" aria-label="Black and white portrait of Ron Brannock"></div>
  <div class="signature">Ron Brannock</div>
  <h1 class="tagline">LEARN PHOTOGRAPHY AND IMAGE EDITING THE EASY WAY</h1>

  <div class="main">
    <nav class="nav">
      <a class="active">HOME</a><a>COURSES</a><a>FREE TUTORIALS</a><a>ABOUT</a><a>CONTACT</a><a style="border-right:none">LOGIN</a>
      <div class="search">Search
        <svg viewBox="0 0 26 24" aria-hidden="true"><circle cx="12" cy="11" r="5" fill="none" stroke="#ddd" stroke-width="2"/><line x1="15.5" y1="14.5" x2="19" y2="18" stroke="#ddd" stroke-width="2"/></svg>
      </div>
    </nav>

    <div class="hero" role="img" aria-label="Carousel photo of two smiling young women outdoors beside a tree">
      <div class="dots"><i></i><i></i><i></i><i></i></div>
    </div>

    <div class="newsletter">
      <p>Subscribe to our Newsletter for New Events, Products &amp; Special Offers</p>
      <div class="email">Enter your Email</div>
      <div class="subscribe">SUBSCRIBE</div>
    </div>

    <div class="feature f1"><div class="thumb" role="img" aria-label="Surfer riding a wave"></div><h3>Lorem ipsum<br>dolor sit<br>amet</h3><span class="more">READ MORE &gt;&gt;</span></div>
    <div class="feature f2"><div class="thumb" role="img" aria-label="Stack of printed portrait photos and a flash unit"></div><h3>Lorem ipsum<br>dolor sit<br>amet</h3><span class="more">READ MORE &gt;&gt;</span></div>
    <div class="feature f3"><div class="thumb" role="img" aria-label="Woman holding a camera"></div><h3>Lorem ipsum<br>dolor sit<br>amet</h3><span class="more">READ MORE &gt;&gt;</span></div>

    <div class="body-copy">
      <p>Lorem ipsum dolor sit amet, consectetuer adipiscing elit. Aenean commodo ligula eget dolor. Aenean massa. Cum sociis natoque penatibus et magnis dis parturient montes, nascetur ridiculus mus. Donec quam felis, ultricies nec, pellentesque eu, pretium quis, sem. Nulla consequat massa quis enim. Donec pede justo, fringilla vel, aliquet nec, vulputate eget, arcu. In enim justo, rhoncus ut, imperdiet a, venenatis vitae, justo. Nullam dictum felis eu pede mollis pretium. Integer tincidunt. Cras dapibus. Vivamus elementum semper nisi. Aenean vulputate eleifend tellus. Aenean leo ligula, porttitor</p>
      <p>Lorem ipsum dolor sit amet, consectetuer adipiscing elit. Aenean commodo ligula eget dolor. Aenean massa. Cum sociis natoque penatibus et magnis dis parturient montes, nascetur ridiculus mus. Donec quam felis, ultricies nec, pellentesque eu, pretium quis, sem. Nulla consequat massa quis enim. Donec pede justo, fringilla vel, aliquet nec, vulputate eget, arcu. In enim justo, rhoncus ut, imperdiet a, venenatis vitae, justo. Nullam dictum felis eu pede mollis pretium. Integer tincidunt. Cras dapibus. Vivamus elementum semper nisi. Aenean vulputate eleifend tellus. Aeneanliquet nec, vulputate eget, arcu. In enim justo, rhoncus ut, imperdiet a, venenatis vitae, justo.</p>
    </div>

    <div class="video" role="img" aria-label="Video still of bridesmaids holding flower bouquets">
      <svg width="50" height="50" viewBox="0 0 50 50" aria-hidden="true"><circle cx="25" cy="25" r="24" fill="rgba(0,0,0,.6)"/><polygon points="20,15 36,25 20,35" fill="#fff"/></svg>
    </div>

    <div class="quote">
      <span class="mark">&ldquo;</span>
      Lorem ipsum dolor sit amet, consectetuer adipiscing elit. Aenean commodo ligula eget
      <svg width="26" height="16" viewBox="0 0 26 16" aria-hidden="true"><polygon points="0,0 26,0 26,16" fill="#444"/></svg>
    </div>
    <div class="author"><strong>Dale Fenwick</strong><span>Freelance photojournalist</span></div>
  </div>

  <footer class="footer">
    <div class="links">Home<span>|</span>Courses<span>|</span>Free Tutorials<span>|</span>About<span>|</span>Contact<span>|</span>privacy policy<span>|</span>affiliates</div>
    <div class="copy">Copyright © 2011 Ron Brannock. All rights reserved. Privacy Policy &nbsp;|&nbsp; Terms of Use</div>
    <div class="social" aria-hidden="true"><i class="dot blue"></i><i class="dot sky"></i><i class="dot orange"></i></div>
  </footer>
</body>
</html>
```